School Hallway Magnetic Display Design for school values

I am looking for a someone to help me design a magnetic hallway display that will hang in the hallway of our small school. There are several elements, including 1. 6ft by 4ft designed magnetic bulletin board, 2. Magnets that will stick to the board. See attachment for which elements belong where. The display will be for our TRAVEK program, which rewards students for demonstrating our school values. We want the display to be beautiful and interactive. We are also rebranding, so we want the design to align with our new fonts and colors. In the attached PDF is an outline of our new brand guidelines. Unfortunately, we don't have the color codes, but I'm hoping that you can match the colors listed. Attached are elements to be used on the board, but please use your creativity to make it more dynamic and visually appealing. For example, the star magnets could be another shape. The TRAVEK magnets must remain the same. I've included two photos of boards at other schools that inspired this project.

Target Market(s)

School Community

Industry/Entity Type

Education

Requirements
Should not have
• School Logo

```html
<!DOCTYPE html>
<html lang="en">
<head>
<meta charset="utf-8">
<title>Travek Of The Month – Hallway Display</title>
<link href="https://fonts.googleapis.com/css2?family=DM+Serif+Display&family=Poppins:wght@700&display=swap" rel="stylesheet">
<style>
  :root{
    --backdrop:#616161;
    --white:#ffffff;
    --salmon:#E08A75;
    --lilac:#BC9AC3;
    --sage:#D6DDB8;
    --butter:#FCD87E;
    --sky:#B2CDE2;
    --navy:#2A5B94;
    --ink:#24507A;
    --shadow:rgba(0,0,0,.38);
  }
  *{margin:0;padding:0;box-sizing:border-box}
  html,body{width:1200px;height:2819px;overflow:hidden;background:var(--backdrop)}
  .canvas{position:relative;width:1200px;height:2819px}

  .board{position:absolute;left:111px;top:72px;width:980px;height:654px;background:var(--white);
    box-shadow:18px 18px 22px var(--shadow);overflow:hidden}
  .board-decor{position:absolute;left:0;top:0;width:210px;height:654px;
    background:linear-gradient(180deg,var(--butter) 0%,var(--ink) 35%,var(--butter) 65%,var(--ink) 100%);
    opacity:.9;clip-path:polygon(0 0,60% 0,100% 30%,70% 55%,100% 80%,60% 100%,0 100%)}
  .board-title{position:absolute;left:171px;top:34px;font-family:"DM Serif Display",serif;font-size:78px;line-height:1;letter-spacing:-1px;white-space:nowrap}
  .t-salmon{color:var(--salmon)} .t-lilac{color:var(--lilac)} .t-sage{color:var(--sage)} .t-butter{color:var(--butter)}
  .thermometer{position:absolute;left:800px;top:160px}

  .section-heading{position:absolute;left:0;width:1200px;text-align:center;font-family:"Poppins",sans-serif;font-weight:700;
    font-size:68px;color:var(--white);letter-spacing:-1.5px}
  .heading-words{top:842px}
  .heading-stars{top:1966px}

  .magnet{position:absolute;width:288px;height:374px;border-radius:24px;box-shadow:16px 16px 20px var(--shadow);overflow:hidden;color:var(--white)}
  .magnet-icon{position:absolute;left:114px;top:100px;width:60px;height:70px}
  .magnet-word{position:absolute;left:0;right:0;top:186px;text-align:center;font-family:"DM Serif Display",serif;font-size:41px;line-height:1}
  .magnet-leaf{position:absolute;right:0;bottom:0;width:144px;height:80px;border-radius:80px 0 0 0;background:rgba(255,255,255,.18)}
  .m-simplicity{left:120px;top:1037px;background:var(--salmon)}
  .m-peace{left:440px;top:1042px;background:var(--lilac)}
  .m-integrity{left:759px;top:1037px;background:var(--sage)}
  .m-community{left:120px;top:1444px;background:var(--butter)}
  .m-equality{left:440px;top:1449px;background:var(--sky)}
  .m-stewardship{left:759px;top:1452px;background:var(--navy)}

  .star{position:absolute;width:196px;height:190px;filter:drop-shadow(14px 14px 12px var(--shadow))}
</style>
</head>
<body>
<div class="canvas">

  <section class="board">
    <div class="board-decor" role="img" aria-label="Decorative navy leaves and yellow concentric circle pattern"></div>
    <h1 class="board-title"><span class="t-salmon">Travek</span> <span class="t-lilac">Of</span> <span class="t-sage">The</span> <span class="t-butter">Month</span></h1>
    <svg class="thermometer" width="160" height="450" viewBox="0 0 160 450" fill="none" stroke="var(--ink)" stroke-width="4" stroke-linecap="round">
      <path d="M68 422 A66 66 0 1 1 110 422 Z" stroke="none"/>
      <path d="M66 296 V30 A23 23 0 0 1 112 30 V296 A68 68 0 1 1 66 296 Z"/>
      <g stroke-width="7">
        <line x1="16" y1="22" x2="38" y2="22"/>
        <line x1="30" y1="50" x2="38" y2="50"/>
        <line x1="30" y1="78" x2="38" y2="78"/>
        <line x1="30" y1="106" x2="38" y2="106"/>
        <line x1="30" y1="134" x2="38" y2="134"/>
        <line x1="16" y1="162" x2="38" y2="162"/>
        <line x1="30" y1="190" x2="38" y2="190"/>
        <line x1="30" y1="218" x2="38" y2="218"/>
        <line x1="30" y1="246" x2="38" y2="246"/>
        <line x1="30" y1="274" x2="38" y2="274"/>
        <line x1="16" y1="302" x2="38" y2="302"/>
      </g>
    </svg>
  </section>

  <h2 class="section-heading heading-words">Word magnets</h2>

  <div class="magnet m-simplicity">
    <svg class="magnet-icon" viewBox="0 0 60 70" fill="none" stroke="#fff" stroke-width="5"><circle cx="30" cy="30" r="22"/><circle cx="30" cy="30" r="8" fill="#fff"/><line x1="2" y1="62" x2="58" y2="62"/></svg>
    <div class="magnet-word">Simplicity</div><div class="magnet-leaf"></div>
  </div>
  <div class="magnet m-peace">
    <svg class="magnet-icon" viewBox="0 0 60 70" fill="#fff"><path d="M30 62 L6 36 A14 14 0 0 1 30 16 A14 14 0 0 1 54 36 Z"/></svg>
    <div class="magnet-word">Peace</div><div class="magnet-leaf"></div>
  </div>
  <div class="magnet m-integrity">
    <svg class="magnet-icon" viewBox="0 0 60 70" fill="none" stroke="#fff" stroke-width="6"><path d="M34 10 A24 24 0 1 0 34 60"/><circle cx="48" cy="14" r="4" fill="#fff"/><circle cx="54" cy="35" r="4" fill="#fff"/><circle cx="48" cy="56" r="4" fill="#fff"/></svg>
    <div class="magnet-word">Integrity</div><div class="magnet-leaf"></div>
  </div>
  <div class="magnet m-community">
    <svg class="magnet-icon" viewBox="0 0 60 70" fill="none" stroke="#fff" stroke-width="6"><path d="M34 10 A24 24 0 1 0 34 60"/><circle cx="48" cy="14" r="4" fill="#fff"/><circle cx="54" cy="35" r="4" fill="#fff"/><circle cx="48" cy="56" r="4" fill="#fff"/></svg>
    <div class="magnet-word">Community</div><div class="magnet-leaf"></div>
  </div>
  <div class="magnet m-equality">
    <svg class="magnet-icon" viewBox="0 0 60 70" fill="#fff"><circle cx="14" cy="10" r="6"/><circle cx="46" cy="10" r="6"/><rect x="8" y="18" width="12" height="22"/><rect x="40" y="18" width="12" height="22"/><rect x="2" y="44" width="56" height="4"/><path d="M30 48 L20 64 H40 Z"/></svg>
    <div class="magnet-word">Equality</div><div class="magnet-leaf"></div>
  </div>
  <div class="magnet m-stewardship">
    <svg class="magnet-icon" viewBox="0 0 60 70" fill="#fff"><circle cx="20" cy="10" r="6"/><circle cx="40" cy="10" r="6"/><circle cx="30" cy="30" r="7"/><path d="M4 30 V54 L22 66 H38 L56 54 V30 L44 48 H16 Z"/></svg>
    <div class="magnet-word">Stewardship</div><div class="magnet-leaf"></div>
  </div>

  <h2 class="section-heading heading-stars">Star magnets</h2>

  <svg width="0" height="0" style="position:absolute">
    <defs><path id="star" d="M98 18 L122 74 L180 78 L136 118 L150 174 L98 144 L46 174 L60 118 L16 78 L74 74 Z"/></defs>
  </svg>
  <svg class="star" style="left:282px;top:2171px" viewBox="0 0 196 190"><use href="#star" fill="var(--butter)" stroke="var(--butter)" stroke-width="26" stroke-linejoin="round"/></svg>
  <svg class="star" style="left:502px;top:2171px" viewBox="0 0 196 190"><use href="#star" fill="var(--butter)" stroke="var(--butter)" stroke-width="26" stroke-linejoin="round"/></svg>
  <svg class="star" style="left:721px;top:2171px" viewBox="0 0 196 190"><use href="#star" fill="var(--butter)" stroke="var(--butter)" stroke-width="26" stroke-linejoin="round"/></svg>
  <svg class="star" style="left:282px;top:2378px" viewBox="0 0 196 190"><use href="#star" fill="var(--butter)" stroke="var(--butter)" stroke-width="26" stroke-linejoin="round"/></svg>
  <svg class="star" style="left:502px;top:2378px" viewBox="0 0 196 190"><use href="#star" fill="var(--butter)" stroke="var(--butter)" stroke-width="26" stroke-linejoin="round"/></svg>
  <svg class="star" style="left:721px;top:2378px" viewBox="0 0 196 190"><use href="#star" fill="var(--butter)" stroke="var(--butter)" stroke-width="26" stroke-linejoin="round"/></svg>

</div>
</body>
</html>
```